Create a memorable Stationary for Security Software Company

TelVandrik is the worldwide leader in securing the Internet. Making Internet communications and critical data secure, reliable and available everywhere has been and continues to be our ongoing vision. We are committed to staying focused on real customer needs and to developing new and innovative security solutions that redefine the security landscape.

Industry/Entity Type

Internet

Font styles to use
Serif
Sans Serif
Script

Colors
0792cd
33a6d7
85cae6

```html
<!DOCTYPE html>
<html lang="en">
<head>
<meta charset="utf-8">
<title>TelVandrik Business Card</title>
<link href="https://fonts.googleapis.com/css2?family=Source+Sans+3:wght@400;600&display=swap" rel="stylesheet">
<style>
  :root {
    --page-bg: #9a9a9a;
    --front-bg: #74b2d5;
    --back-bg: #2e8fc4;
    --band-fill: #3f98cb;
    --brand-front: #2a80b8;
    --brand-back: #2380b5;
    --name-blue: #1f6fa0;
    --text-grey: #3f4a52;
    --rule: #2f7fb0;
    --back-web: #93c9e4;
  }
  * { margin: 0; padding: 0; box-sizing: border-box; }
  html, body { width: 1105px; height: 1200px; overflow: hidden; }
  body {
    background: var(--page-bg);
    font-family: "Source Sans 3", Arial, sans-serif;
    position: relative;
  }
  .card {
    position: absolute;
    left: 182px;
    width: 746px;
    height: 427px;
    overflow: hidden;
  }
  .card-front { top: 119px; background: var(--front-bg); }
  .card-back { top: 637px; background: var(--back-bg); }

  .brand {
    position: absolute;
    display: flex;
    align-items: center;
    gap: 12px;
    font-weight: 600;
    font-size: 34px;
    letter-spacing: 0.5px;
    white-space: nowrap;
  }
  .brand-dot { width: 40px; height: 40px; border-radius: 50%; flex: none; }
  .card-front .brand { left: 38px; top: 92px; color: var(--brand-front); }
  .card-front .brand-dot { background: var(--brand-front); }
  .card-back .brand { left: 50%; top: 200px; transform: translateX(-50%); color: var(--brand-back); }
  .card-back .brand-dot { background: var(--brand-back); }

  .person { position: absolute; right: 40px; top: 205px; text-align: right; }
  .person-name { color: var(--name-blue); font-weight: 600; font-size: 27px; line-height: 1.1; }
  .person-role { color: var(--text-grey); font-size: 19px; line-height: 1.3; }

  .rule {
    position: absolute; left: 32px; top: 260px;
    width: 531px; height: 1.5px; background: var(--rule);
  }

  .contacts { position: absolute; left: 34px; top: 280px; list-style: none; }
  .contacts li {
    display: flex; align-items: center; gap: 12px;
    color: var(--text-grey); font-size: 19px; height: 28.5px;
  }
  .contacts svg { width: 17px; height: 17px; fill: var(--name-blue); }

  .address {
    position: absolute; right: 40px; top: 280px; text-align: right;
    color: var(--text-grey); font-size: 19px; line-height: 28.5px;
  }

  .bottom-band {
    position: absolute; left: 0; bottom: 0;
    width: 746px; height: 38px;
    background: var(--band-fill);
  }

  .back-web {
    position: absolute; left: 0; right: 0; top: 360px; text-align: center;
    color: var(--back-web); font-size: 17px; letter-spacing: 4px;
  }
</style>
</head>
<body>

<section class="card card-front">
  <div class="brand"><span class="brand-dot"></span><span class="brand-name">TelVandrik</span></div>

  <div class="person">
    <div class="person-name">Dara Quillon</div>
    <div class="person-role">CEO/Founder</div>
  </div>

  <div class="rule"></div>

  <ul class="contacts">
    <li>
      <svg viewBox="0 0 24 24" aria-hidden="true"><path d="M6.6 10.8a15.1 15.1 0 0 0 6.6 6.6l2.2-2.2a1 1 0 0 1 1-.25 11.4 11.4 0 0 0 3.6.57 1 1 0 0 1 1 1V20a1 1 0 0 1-1 1A17 17 0 0 1 3 4a1 1 0 0 1 1-1h3.5a1 1 0 0 1 1 1c0 1.250.2 2.45.57 3.57a1 1 0 0 1-.25 1z"/></svg>
      614 205 7391
    </li>
    <li>
      <svg viewBox="0 0 24 24" aria-hidden="true"><path d="M6 2h12v5H6zM3 8h18a1 1 0 0 1 1 1v7h-4v-3H6v3H2V9a1 1 0 0 1 1-1zm3 6h12v8H6z"/></svg>
      614 205 7392
    </li>
    <li>
      <svg viewBox="0 0 24 24" aria-hidden="true"><path d="M2 5h20v14H2zm2 2v.5l8 5 8-5V7l-8 5z"/></svg>
      hello@telvandrik.net
    </li>
  </ul>

  <div class="address">
    2190 Larkspur Way<br>
    Fairbanks, Alaska 99701<br>
    www.telvandrik.net
  </div>

  <div class="bottom-band" role="img" aria-label="Decorative cloud border along the bottom edge"></div>
</section>

<section class="card card-back">
  <div class="brand"><span class="brand-dot"></span><span class="brand-name">TelVandrik</span></div>
  <div class="back-web">www.telvandrik.net</div>
</section>

</body>
</html>
```